Bright Prospect Hub

I would like 4 different size banner ads. The "Standard" online sizes. I believe they are: 125x125 | 728x90 | 468x60 | 250x250 These banners will be for promoting the website. I want to make sure you can read what the banners say so NO real fancy text. I've uploaded a few ideas as I do want them to kinda look like the website. https://www.brightprospecthub.com/ Take a look at the site and you will see we use money bags, dollar signs and bright colors.

```html
<!DOCTYPE html>
<html lang="en">
<head>
<meta charset="utf-8">
<title>Bright Prospect Hub – Banner Set</title>
<link href="https://fonts.googleapis.com/css2?family=Cinzel:wght@700;900&family=Oswald:wght@400;500&display=swap" rel="stylesheet">
<style>
  :root {
    --board: #5a3620;
    --label: #f3ece4;
    --frame: #2aa6df;
    --paper: #ffffff;
    --head-a: #19b3cf;
    --head-b: #1f5ea8;
    --red: #e8161b;
    --olive: #66741f;
    --ink: #111111;
    --arrow: #f4d13a;
    --arrow-edge: #2aa6df;
    --hand: #f2c14e;
    --bag: #6d8a34;
  }
  * { margin: 0; padding: 0; box-sizing: border-box; }
  html, body { width: 1200px; height: 415px; overflow: hidden; }
  body { background: var(--board); position: relative; font-family: "Oswald", sans-serif; }

  .banner { position: absolute; background: var(--paper); border: 2px solid var(--frame); overflow: hidden; }
  .banner > * { position: absolute; white-space: nowrap; }
  .size-label { position: absolute; color: var(--label); font-size: 14px; font-family: "Oswald", sans-serif; }

  .headline {
    font-family: "Cinzel", serif; font-weight: 900; line-height: 1;
    background: linear-gradient(180deg, var(--head-a), var(--head-b));
    -webkit-background-clip: text; background-clip: text; color: transparent;
  }
  .tagline { color: var(--red); font-weight: 400; line-height: 1; }
  .tagline.dark { color: var(--ink); }
  .unlimited { font-family: "Cinzel", serif; font-weight: 700; color: var(--red); line-height: 1; }
  .ongoing { color: var(--olive); font-weight: 400; line-height: 1; }
  .pointer { background: linear-gradient(90deg, #f7d77a, var(--hand)); border-radius: 40% 20% 20% 40%; }
  .money-bag { background: radial-gradient(circle at 55% 55%, var(--bag), #f0c24a 90%); border-radius: 45% 45% 40% 40%; }
  .swoosh { display: block; }

  /* 125x125 */
  .b125 { left: 45px; top: 28px; width: 142px; height: 142px; }
  .b125 .pointer { left: 6px; top: 7px; width: 26px; height: 14px; }
  .b125 .h1 { left: 38px; top: 4px; font-size: 20px; }
  .b125 .h2 { left: 6px; top: 27px; font-size: 15px; }
  .b125 .tagline { left: 0; right: 0; top: 50px; text-align: center; font-size: 10px; }
  .b125 .arrow { left: 62px; top: 63px; }
  .b125 .unlimited { left: 0; right: 0; top: 82px; text-align: center; font-size: 12px; }
  .b125 .money-bag { left: 6px; top: 102px; width: 28px; height: 30px; }
  .b125 .ongoing { left: 40px; top: 109px; font-size: 13px; }
  .b125 .swoosh { left: 40px; top: 127px; }

  /* 468x60 */
  .b468 { left: 214px; top: 77px; width: 536px; height: 71px; }
  .b468 .pointer { left: 7px; top: 9px; width: 36px; height: 15px; }
  .b468 .headline { left: 48px; top: 8px; font-size: 19px; }
  .b468 .tagline { left: 8px; top: 36px; font-size: 21px; }
  .b468 .money-bag { left: 300px; top: 10px; width: 52px; height: 50px; }
  .b468 .unlimited { left: 364px; top: 9px; font-size: 15px; }
  .b468 .ongoing { left: 368px; top: 31px; font-size: 21px; }
  .b468 .swoosh { left: 370px; top: 58px; }

  /* 728x90 */
  .b728 { left: 32px; top: 250px; width: 832px; height: 105px; }
  .b728 .pointer { left: 8px; top: 13px; width: 50px; height: 22px; }
  .b728 .headline { left: 64px; top: 11px; font-size: 28px; }
  .b728 .tagline { left: 10px; top: 50px; font-size: 31px; }
  .b728 .money-bag { left: 452px; top: 20px; width: 88px; height: 74px; }
  .b728 .unlimited { left: 556px; top: 14px; font-size: 22px; }
  .b728 .ongoing { left: 576px; top: 48px; font-size: 31px; }
  .b728 .swoosh { left: 578px; top: 88px; }

  /* 250x250 */
  .b250 { left: 875px; top: 62px; width: 289px; height: 286px; }
  .b250 .pointer { left: 12px; top: 22px; width: 52px; height: 28px; }
  .b250 .h1 { left: 86px; top: 14px; font-size: 40px; }
  .b250 .h2 { left: 0; right: 0; top: 60px; text-align: center; font-size: 27px; }
  .b250 .tagline { left: 0; right: 0; top: 98px; text-align: center; font-size: 18px; }
  .b250 .arrow { left: 128px; top: 124px; }
  .b250 .unlimited { left: 0; right: 0; top: 166px; text-align: center; font-size: 25px; }
  .b250 .money-bag { left: 10px; top: 200px; width: 66px; height: 66px; }
  .b250 .ongoing { left: 84px; top: 222px; font-size: 25px; }
  .b250 .swoosh { left: 86px; top: 256px; }
</style>
</head>
<body>

<div class="banner b125">
  <div class="pointer" role="img" aria-label="Pointing hand illustration"></div>
  <div class="headline h1">BRIGHT</div>
  <div class="headline h2">PROSPECT HUB</div>
  <div class="tagline dark">Plus, A Monthly Residual Income!</div>
  <svg class="arrow" width="18" height="18" viewBox="0 0 18 18"><path d="M6 1h6v8h5l-8 8-8-8h5z" fill="var(--arrow)" stroke="var(--arrow-edge)" stroke-width="1"/></svg>
  <div class="unlimited">TRULY UNLIMITED</div>
  <div class="money-bag" role="img" aria-label="Money bag with gold coins illustration"></div>
  <div class="ongoing">ONGOING INCOME!</div>
  <svg class="swoosh" width="60" height="8" viewBox="0 0 60 8"><path d="M1 6 Q30 0 59 3" stroke="var(--red)" stroke-width="2.5" fill="none" stroke-linecap="round"/></svg>
</div>
<div class="size-label" style="left:74px;top:181px">125x125</div>

<div class="banner b468">
  <div class="pointer" role="img" aria-label="Pointing hand illustration"></div>
  <div class="headline">BRIGHT PROSPECT HUB</div>
  <div class="tagline">Plus, A Monthly Residual Income!</div>
  <div class="money-bag" role="img" aria-label="Money bag with gold coins illustration"></div>
  <div class="unlimited">TRULY UNLIMITED</div>
  <div class="ongoing">ONGOING INCOME!</div>
  <svg class="swoosh" width="80" height="8" viewBox="0 0 80 8"><path d="M1 6 Q40 0 79 3" stroke="var(--red)" stroke-width="3" fill="none" stroke-linecap="round"/></svg>
</div>
<div class="size-label" style="left:483px;top:164px">468x60</div>

<div class="banner b728">
  <div class="pointer" role="img" aria-label="Pointing hand illustration"></div>
  <div class="headline">BRIGHT PROSPECT HUB</div>
  <div class="tagline">Plus, A Monthly Residual Income!</div>
  <div class="money-bag" role="img" aria-label="Money bag with gold coins illustration"></div>
  <div class="unlimited">TRULY UNLIMITED</div>
  <div class="ongoing">ONGOING INCOME!</div>
  <svg class="swoosh" width="110" height="10" viewBox="0 0 110 10"><path d="M1 8 Q55 0 109 4" stroke="var(--red)" stroke-width="3.5" fill="none" stroke-linecap="round"/></svg>
</div>
<div class="size-label" style="left:45px;top:366px">728x90</div>

<div class="banner b250">
  <div class="pointer" role="img" aria-label="Pointing hand illustration"></div>
  <div class="headline h1">BRIGHT</div>
  <div class="headline h2">PROSPECT HUB</div>
  <div class="tagline dark">Plus, A Monthly Residual Income!</div>
  <svg class="arrow" width="30" height="36" viewBox="0 0 30 36"><path d="M10 1h10v19h9L15 35 1 20h9z" fill="var(--arrow)" stroke="var(--arrow-edge)" stroke-width="1.5"/></svg>
  <div class="unlimited">TRULY UNLIMITED</div>
  <div class="money-bag" role="img" aria-label="Money bag with gold coins illustration"></div>
  <div class="ongoing">ONGOING INCOME!</div>
  <svg class="swoosh" width="90" height="10" viewBox="0 0 90 10"><path d="M1 8 Q45 0 89 4" stroke="var(--red)" stroke-width="3" fill="none" stroke-linecap="round"/></svg>
</div>
<div class="size-label" style="left:986px;top:360px">250x250</div>

</body>
</html>
```